Biz Cards for Lumivale Associates

Lumivale Associates is seeking a single-sided business card that is more visually-appealing than our current design (see attached).

Notes:
- Our colors are blue & teal.
- Our tag line must be large enough to be easily read
- We don't necessarily need our address included (that's just the biz office)
- We'd like to add our email address: Lumivale512@brindlemail.net

Thanks!

Industry/Entity Type

Business

Contact Information for Business Card

Standard size
PSD file required w/ text on its own layer

Colors
86cfc6
3277b5

```html
<!DOCTYPE html>
<html lang="en">
<head>
<meta charset="utf-8">
<title>Lumivale Associates – Business Card</title>
<link href="https://fonts.googleapis.com/css2?family=Raleway:wght@400;500;600&display=swap" rel="stylesheet">
<style>
  :root {
    --page-bg: #d8d3cb;
    --card-bg: #f2f1ee;
    --card-edge: #e2e0dc;
    --brand-blue: #3277b5;
    --brand-teal: #86cfc6;
    --icon-teal: #2fa394;
    --navy: #2d5d8c;
    --grey-text: #6d6d6d;
    --ring: #2b2b2b;
  }
  * { margin: 0; padding: 0; box-sizing: border-box; }
  html, body { width: 1200px; height: 1047px; overflow: hidden; }
  body {
    background: var(--page-bg);
    font-family: "Raleway", sans-serif;
    position: relative;
  }
  .business-card {
    position: absolute;
    left: 100px; top: 253px;
    width: 1000px; height: 540px;
    background: var(--card-bg);
    border: 1px solid var(--card-edge);
    border-radius: 24px;
    overflow: hidden;
  }
  .brand-lockup {
    position: absolute;
    left: 40px; top: 112px;
    display: flex; align-items: center; gap: 14px;
  }
  .brand-dot {
    width: 34px; height: 34px;
    border: 2px solid var(--ring);
    border-radius: 50%;
  }
  .brand-name {
    font-size: 34px; font-weight: 500;
    color: var(--ring);
    letter-spacing: 0.5px;
  }
  .person-name {
    position: absolute; left: 40px; top: 220px;
    font-size: 28px; font-weight: 500;
    color: var(--brand-blue);
  }
  .person-title {
    position: absolute; left: 40px; top: 262px;
    font-size: 21px; font-weight: 500;
    color: var(--grey-text);
    letter-spacing: 0.3px;
  }
  .contact-list {
    position: absolute; left: 40px; top: 335px;
    list-style: none;
  }
  .contact-item {
    display: flex; align-items: center;
    height: 30.5px;
    font-size: 21px; font-weight: 400;
    color: var(--grey-text);
  }
  .contact-icon {
    width: 20px; height: 20px;
    margin-right: 20px;
    fill: var(--icon-teal);
  }
  .tagline {
    position: absolute; left: 38px; top: 482px;
    font-size: 22px; font-weight: 600;
    color: var(--navy);
  }
  .tagline .sep { color: var(--icon-teal); font-weight: 400; margin: 0 4px; }
  .deco-ring {
    position: absolute;
    left: 590px; top: 146px;
    width: 490px; height: 490px;
    border: 5px solid var(--ring);
    border-radius: 50%;
    display: flex; align-items: center; justify-content: center;
  }
  .deco-fill {
    width: 400px; height: 400px;
    border-radius: 50%;
    background: radial-gradient(circle, var(--brand-teal) 0%, var(--brand-blue) 100%);
    opacity: 0.45;
  }
</style>
</head>
<body>
  <div class="business-card">
    <div class="brand-lockup">
      <span class="brand-dot"></span>
      <span class="brand-name">Lumivale Associates</span>
    </div>

    <div class="person-name">Dana Whitcomb, RN</div>
    <div class="person-title">Mental Health Therapist</div>

    <ul class="contact-list">
      <li class="contact-item">
        <svg class="contact-icon" viewBox="0 0 20 20"><path d="M6 1h8a1.5 1.5 0 0 1 1.5 1.5v15A1.5 1.5 0 0 1 14 19H6a1.5 1.5 0 0 1-1.5-1.5v-15A1.5 1.5 0 0 1 6 1zm0 2.5v11h8v-11zm4 12.3a1 1 0 1 0 0 2 1 1 0 0 0 0-2z"/></svg>
        (855) LUM-VALE
      </li>
      <li class="contact-item">
        <svg class="contact-icon" viewBox="0 0 20 20"><path d="M5 2h10v4H5zM2 7h16a1 1 0 0 1 1 1v7h-3v-3H4v3H1V8a1 1 0 0 1 1-1zm3 6h10v5H5z"/></svg>
        (330) 555-0187
      </li>
      <li class="contact-item">
        <svg class="contact-icon" viewBox="0 0 20 20"><path d="M1 4h18v2l-9 5-9-5zm0 4.3 9 5 9-5V16H1z"/></svg>
        Lumivale512@brindlemail.net
      </li>
      <li class="contact-item">
        <svg class="contact-icon" viewBox="0 0 20 20"><path d="M8 1a7 7 0 0 1 5.6 11.2l5 5-1.9 1.9-5-5A7 7 0 1 1 8 1zm0 2.6a4.4 4.4 0 1 0 0 8.8 4.4 4.4 0 0 0 0-8.8z"/></svg>
        www.lumivale.net
      </li>
    </ul>

    <div class="tagline">Steady Minds<span class="sep">|</span>Open Hearts<span class="sep">|</span>Better Days</div>

    <div class="deco-ring">
      <div class="deco-fill" role="img" aria-label="Large decorative brand mark area in blue and teal"></div>
    </div>
  </div>
</body>
</html>
```